Branvique needs a business Card Design

We are looking for a business card Design for our new Managed Service Provider Company, Branvique. Branvique encompasses everything IT for the average medium sized business. Our primary services are help desk support, cyber-security (malware and ransomware protection), and Disaster Recovery systems. We would like the design to have a very clean and professional look, with a very minimalist feel.

Target Market(s)

Medium to large sized businesses

Industry/Entity Type

It Service

Contact Information for Business Card

Name GoesHere
name@branvique.com
O: 555-382-6047
C: 555-731-5820

Font styles to use
Other font styles liked:
• Poppins Font Only Please

Colors

Designer to choose only greyscale colors for use in the design.

Requirements
Must have
• Logo included
Nice to have
• Cutting Edge, innovative, minimalistic, elegant

```html
<!DOCTYPE html>
<html lang="en">
<head>
<meta charset="UTF-8">
<title>Branvique Business Card</title>
<link href="https://fonts.googleapis.com/css2?family=Poppins:wght@300;400;500&display=swap" rel="stylesheet">
<style>
  :root {
    --page-bg: #e9e7e3;
    --card-light: #ffffff;
    --card-dark: #1c2c43;
    --ink-dark: #1c2c43;
    --ink-light: #ffffff;
    --ink-muted: #3a4658;
    --deco-light: rgba(28, 44, 67, 0.12);
    --deco-dark: rgba(255, 255, 255, 0.07);
    --shadow: rgba(0, 0, 0, 0.28);
  }
  * { margin: 0; padding: 0; box-sizing: border-box; }
  html, body {
    width: 900px;
    height: 1200px;
    overflow: hidden;
  }
  body {
    background: var(--page-bg);
    font-family: "Poppins", sans-serif;
    position: relative;
  }
  .card {
    position: absolute;
    left: 75px;
    width: 750px;
    height: 435px;
    border-radius: 26px;
    box-shadow: 0 10px 24px var(--shadow);
    overflow: hidden;
  }
  .card--front { top: 135px; background: var(--card-light); color: var(--ink-dark); }
  .card--back  { top: 630px; background: var(--card-dark); color: var(--ink-light); }

  .deco-block {
    position: absolute;
    top: 0;
    bottom: 0;
    left: 560px;
    width: 150px;
  }
  .card--front .deco-block {
    background: linear-gradient(to bottom, var(--deco-light) 0%, var(--deco-light) 55%, rgba(28, 44, 67, 0) 90%);
  }
  .card--back .deco-block {
    background: linear-gradient(to bottom, var(--deco-dark) 0%, var(--deco-dark) 60%, rgba(255, 255, 255, 0) 95%);
  }

  .brand {
    position: absolute;
    left: 0;
    right: 0;
    display: flex;
    flex-direction: column;
    align-items: center;
    gap: 46px;
  }
  .card--front .brand { top: 135px; }
  .card--back .brand  { top: 145px; }
  .brand__mark {
    width: 34px;
    height: 34px;
    background: currentColor;
  }
  .brand__name {
    font-weight: 400;
    font-size: 32px;
    line-height: 1;
    letter-spacing: 0.3em;
    text-transform: uppercase;
    padding-left: 0.3em;
  }

  .holder {
    position: absolute;
    top: 330px;
    left: 0;
    right: 0;
    text-align: center;
    font-weight: 500;
    font-size: 21px;
    letter-spacing: 0.12em;
    text-transform: uppercase;
  }
  .contact {
    position: absolute;
    top: 372px;
    left: 0;
    right: 0;
    display: flex;
    justify-content: center;
    gap: 24px;
    font-weight: 400;
    font-size: 14px;
    letter-spacing: 0.03em;
    color: var(--ink-muted);
    text-transform: uppercase;
  }
</style>
</head>
<body>
  <section class="card card--front" aria-label="Business card front">
    <div class="deco-block" aria-hidden="true"></div>
    <div class="brand">
      <span class="brand__mark" aria-hidden="true"></span>
      <span class="brand__name">Branvique</span>
    </div>
    <p class="holder">Name Goeshere</p>
    <p class="contact">
      <span>E: name@branvique.com</span>
      <span>O: 555-382-6047</span>
      <span>C: 555-731-5820</span>
    </p>
  </section>

  <section class="card card--back" aria-label="Business card back">
    <div class="deco-block" aria-hidden="true"></div>
    <div class="brand">
      <span class="brand__mark" aria-hidden="true"></span>
      <span class="brand__name">Branvique</span>
    </div>
  </section>
</body>
</html>
```